Substance abuse awareness flyer for school age kids

I am needing a flyer for school-age kids. What if it were designed to look like an Travlo with someone texting and the text bubbles were some of the text below with emojis? Maybe a text chain between to friends:

Maybe the first text bubble says "I'm thinking about using drugs and alcohol"
the next bubble: "Just say no!" ( perhaps a stop sign emoji ?)

"Talk to your parents, your teachers at school, or your doctor about how drugs and alcohol can harm you"

another text bubble "did you know that alcohol and drugs could lead to..."
then include some of the info below (see links for more info).
Where ever you get info, it must be cited.

this needs to be English on one side and Spanish on the other side and needs to include the logo attached.

The effects of substance abuse
BWR: https://www.bwr-example.org/kvtmpl/yrnq/articles/youth-risk-habits.html
Affect growth and development, especially brain development. Not able to focus at school or be around friends. https://www.healthyminds-sample.org/pages/shared/docs/stayingclear_2.pdf
Leads to risky behaviors and lack of impulse control (dangerous activities) https://www.healthyminds-sample.org/pages/shared/docs/stayingclear_2.pdf
Contribute to health problems as an adult: heart disease, high blood pressure, and trouble sleeping.

Target Market(s)

school age kids 9-20

Requirements
Must have
• Print ready: 8.5x11

```html
<!DOCTYPE html>
<html lang="en">
<head>
<meta charset="utf-8">
<title>Teen Substance Use &amp; Risks</title>
<link href="https://fonts.googleapis.com/css2?family=Rubik:wght@500;600&family=Roboto:wght@400;500;700&family=Indie+Flower&display=swap" rel="stylesheet">
<style>
  :root {
    --cream: #fdf7ee;
    --coral: #f98a84;
    --coral-line: #f07a78;
    --violet: #6c70ea;
    --ink: #4a4a4a;
    --ink-dark: #333333;
    --peach-disc: #f8eade;
    --soft-blob: #fbeee4;
    --letter-orange: #f6b04a;
    --letter-violet: #7a75ea;
    --letter-coral: #f47f78;
    --phone-body: #efeeeb;
    --phone-edge: #cfcdc8;
    --screen: #f4f1ea;
    --bar-orange: #eb9a1a;
    --bubble: #bfe7ea;
    --bubble-edge: #2f8fb6;
    --skin-light: #f6dccb;
    --skin: #efc3a6;
    --book-tone: #8b6fc6;
    --lens-tone: #6fc5ef;
  }
  * { margin: 0; padding: 0; box-sizing: border-box; }
  html, body { width: 848px; height: 1200px; overflow: hidden; background: var(--cream); }
  .flyer { position: relative; width: 848px; height: 1200px; overflow: hidden; background: var(--cream); font-family: "Roboto", sans-serif; }
  .abs { position: absolute; }

  .decor-layer { left: 0; top: 0; width: 848px; height: 1200px; z-index: 0; }

  .hand-photo { left: 318px; top: 590px; width: 530px; height: 610px; z-index: 0;
    background: radial-gradient(ellipse 70% 75% at 65% 55%, var(--skin) 0%, var(--skin-light) 60%, rgba(253,247,238,0) 100%); }

  .brand-disc { left: 549px; top: 19px; width: 258px; height: 258px; border-radius: 50%; background: var(--peach-disc); display: flex; align-items: center; justify-content: center; gap: 8px; }
  .brand-dot { width: 14px; height: 14px; border-radius: 50%; background: var(--violet); flex: none; }
  .brand-name { font-family: "Roboto", sans-serif; font-weight: 700; font-size: 17px; line-height: 1.2; color: var(--violet); }

  .float-letter { font-family: "Rubik", sans-serif; font-weight: 600; font-size: 34px; line-height: 1; z-index: 2; }
  .float-letter--b1 { left: 294px; top: 406px; color: var(--letter-orange); transform: rotate(-14deg); }
  .float-letter--a { left: 165px; top: 480px; color: var(--letter-violet); transform: rotate(8deg); }
  .float-letter--c { left: 282px; top: 533px; color: var(--letter-coral); }
  .float-letter--b2 { left: 283px; top: 838px; color: var(--letter-orange); transform: rotate(-12deg); }

  .text { z-index: 3; }
  .title { left: 25px; top: 590px; font-family: "Rubik", sans-serif; font-weight: 600; font-size: 35px; line-height: 46px; color: var(--violet); }
  .intro { left: 25px; top: 702px; width: 284px; font-size: 14px; line-height: 17px; color: var(--ink); }
  .effect { left: 25px; font-family: "Rubik", sans-serif; font-weight: 600; font-size: 18.4px; line-height: 24px; color: var(--violet); }
  .effect--growth { top: 892px; }
  .effect--risk { top: 1004px; left: 24px; }
  .source { left: 25px; top: 1068px; font-size: 13px; color: var(--ink); }
  .footnote { left: 25px; top: 1158px; font-size: 13px; font-weight: 700; color: var(--ink-dark); white-space: nowrap; }

  .phone { left: 359px; top: 401px; width: 291px; height: 605px; border-radius: 46px; background: var(--phone-body); border: 2px solid var(--phone-edge); z-index: 1; }
  .phone-speaker { left: 123px; top: 36px; width: 42px; height: 4px; border-radius: 2px; background: #222; }
  .phone-camera { left: 99px; top: 33px; width: 8px; height: 8px; border-radius: 50%; background: #222; }
  .phone-sensor { left: 141px; top: 17px; width: 6px; height: 6px; border-radius: 50%; background: #222; }
  .phone-home { left: 120px; top: 543px; width: 46px; height: 46px; border-radius: 50%; border: 2px solid var(--phone-edge); }

  .screen { left: 373px; top: 472px; width: 262px; height: 460px; background: var(--screen); border: 2px solid #222; overflow: hidden; z-index: 2; }
  .status-bar { left: 0; top: 0; width: 100%; height: 22px; background: var(--bar-orange); color: #fbe6c4; font-size: 9px; display: flex; justify-content: flex-end; align-items: center; padding: 0 8px; }
  .chat-header { left: 0; top: 22px; width: 100%; height: 36px; background: var(--bar-orange); color: #fff; display: flex; align-items: center; padding: 0 12px; gap: 14px; font-size: 15px; }
  .chat-header .contact { flex: 1; }
  .chat-header svg { display: block; }

  .bubble { background: var(--bubble); border: 2px dashed var(--bubble-edge); border-radius: 50%; font-family: "Indie Flower", cursive; color: #1d1d1d; text-align: center; display: flex; align-items: center; justify-content: center; letter-spacing: 0.3px; }
  .bubble--first { left: 14px; top: 63px; width: 220px; height: 70px; font-size: 15px; line-height: 21.5px; }
  .bubble--second { left: 25px; top: 147px; width: 224px; height: 154px; font-size: 15px; line-height: 21.5px; border-radius: 48%; }
  .bubble--third { left: 12px; top: 330px; width: 222px; height: 74px; font-size: 15px; line-height: 21.5px; }
  .stop-icon { display: inline-block; vertical-align: -2px; margin-left: 6px; }

  .avatar { width: 28px; height: 28px; border-radius: 50%; background: #9ccfd6; border: 2px solid #d9eef0; }
  .avatar--friend { left: 10px; top: 141px; }
  .avatar--me { left: 225px; top: 321px; }

  .composer { left: 0; top: 424px; width: 100%; height: 34px; display: flex; align-items: center; padding: 0 6px 0 10px; gap: 8px; font-size: 12px; color: #8a8a8a; }
  .composer .field { flex: 1; }
  .send-btn { width: 30px; height: 28px; background: var(--bar-orange); color: #f7c07a; font-size: 8px; display: flex; align-items: center; justify-content: center; }
</style>
</head>
<body>
<main class="flyer">

  <svg class="abs decor-layer" width="848" height="1200" viewBox="0 0 848 1200" aria-hidden="true">
    <path d="M0 0 H518 C522 70 500 140 440 170 C380 200 310 175 250 200 C190 225 210 300 160 360 C120 400 60 410 0 400 Z" fill="var(--coral)"/>
    <path d="M0 430 C70 445 140 430 180 385" fill="none" stroke="var(--coral-line)" stroke-width="2.5" stroke-dasharray="12 9"/>
    <path d="M255 205 C300 195 360 195 420 180 C460 170 500 140 520 100 C535 60 540 30 540 0" fill="none" stroke="var(--coral-line)" stroke-width="2.5" stroke-dasharray="12 9"/>
    <path d="M0 560 C80 490 190 520 220 640 L220 960 L0 960 Z" fill="var(--soft-blob)"/>
  </svg>

  <div class="abs hand-photo" role="img" aria-label="Photo of a hand holding the phone"></div>

  <svg class="abs" style="left:14px;top:66px" width="262" height="306" viewBox="0 0 262 306" role="img" aria-label="Illustration of a closed purple notebook">
    <rect x="20" y="20" width="200" height="260" rx="14" transform="rotate(-20 120 150)" fill="var(--book-tone)"/>
  </svg>
  <svg class="abs" style="left:276px;top:28px" width="226" height="166" viewBox="0 0 226 166" role="img" aria-label="Illustration of a magnifying glass">
    <circle cx="150" cy="90" r="72" fill="var(--lens-tone)"/>
  </svg>

  <div class="abs brand-disc">
    <span class="brand-dot"></span>
    <span class="brand-name">Riverbend<br>Care Network</span>
  </div>

  <span class="abs float-letter float-letter--b1">B</span>
  <span class="abs float-letter float-letter--a">A</span>
  <span class="abs float-letter float-letter--c">C</span>
  <span class="abs float-letter float-letter--b2">B</span>

  <div class="abs phone" aria-hidden="true">
    <span class="abs phone-sensor"></span>
    <span class="abs phone-camera"></span>
    <span class="abs phone-speaker"></span>
    <span class="abs phone-home"></span>
  </div>

  <section class="abs screen" aria-label="Text conversation">
    <div class="abs status-bar">10:23 AM</div>
    <header class="abs chat-header">
      <svg width="14" height="12" viewBox="0 0 14 12" aria-hidden="true"><path d="M13 6H2M6 1L1 6l5 5" fill="none" stroke="#fff" stroke-width="1.8"/></svg>
      <span class="contact">40218</span>
      <svg width="12" height="12" viewBox="0 0 12 12" aria-hidden="true"><path d="M2 1h3l1 3-1.5 1a7 7 0 0 0 2.5 2.5L8 6l3 1v3c0 1-1 1-1 1A9 9 0 0 1 1 2s0-1 1-1z" fill="#fff"/></svg>
      <svg width="10" height="12" viewBox="0 0 10 12" aria-hidden="true"><path d="M0 2h10M3 2V0h4v2M1 3h8l-1 9H2z" fill="#fff"/></svg>
      <svg width="4" height="12" viewBox="0 0 4 12" aria-hidden="true"><circle cx="2" cy="2" r="1.5" fill="#fff"/><circle cx="2" cy="6" r="1.5" fill="#fff"/><circle cx="2" cy="10" r="1.5" fill="#fff"/></svg>
    </header>

    <p class="abs bubble bubble--first">I’m thinking about<br>using drugs and alcohol</p>
    <span class="abs avatar avatar--friend"></span>
    <p class="abs bubble bubble--second">
      <span>Just say no!<svg class="stop-icon" width="14" height="14" viewBox="0 0 14 14" aria-label="no"><circle cx="7" cy="7" r="5.5" fill="none" stroke="#d5283a" stroke-width="2"/><path d="M3 3l8 8" stroke="#d5283a" stroke-width="2"/></svg><br>Talk to your parents,<br>your teachers at school,<br>or your doctor about<br>how drugs and alcohol<br>can harm you</span>
    </p>
    <span class="abs avatar avatar--me"></span>
    <p class="abs bubble bubble--third">did you know that alcohol<br>and drugs could lead to?</p>

    <div class="abs composer">
      <svg width="14" height="14" viewBox="0 0 14 14" aria-hidden="true"><path d="M9 3L4 9a1.5 1.5 0 0 0 2 2l6-6a3 3 0 0 0-4-4L2 7" fill="none" stroke="#888" stroke-width="1.3"/></svg>
      <span class="field">Enter message</span>
      <span class="send-btn">Send</span>
    </div>
  </section>

  <h1 class="abs text title">Teen Substance<br>Use &amp; Risks</h1>

  <p class="abs text intro">Parents play a critical role in their children’s lives. As their children grow to pre-teens and teens, parents worry about new risks they may experience. One such risk is the use of substances, such as alcohol, marijuana, tobacco, and other drugs. Parents can help by talking to their teen’s pediatrician about screening for substance use.</p>

  <p class="abs text effect effect--growth">Affect growth and development,<br>especially brain development.<br>Not able to focus at school<br>or be around friends.</p>
  <p class="abs text effect effect--risk">Leads to risky behaviors and lack<br>of impulse control (dangerous activities)</p>

  <p class="abs text source">www.healthyminds-sample.org/pages/shared/docs/stayingclear_2.pdf</p>
  <p class="abs text footnote">Contribute to health problems as an adult: heart disease, high blood pressure, and trouble sleeping.</p>

</main>
</body>
</html>
```